The name of the company is Kestrel Rehab buying foreclosed homes and remodeling

A sleek classy card. It’s a home remodel and house flip company. Something mostly black with dark gray and red in color . Something with two f”s as a logo on front as shown in pictures. Kind of just let you guys run with it . I left a few pictures that should help
You guys get an idea of what I thought was good also left all the information for back of the card

Target Market(s)

Home remodel consumers

Industry/Entity Type

Construction Company

Contact Information for Business Card

All details are on photo

Font styles to use
Decorative

Colors

Designer to choose colors to be used in the design.

Requirements
Must have
• Name of company on front. Kestrel Rehab
Nice to have
• Up to you guys I trust you
Should not have
• Not sure

```html
<!DOCTYPE html>
<html lang="en">
<head>
<meta charset="utf-8">
<title>Kestrel Rehab – Business Card</title>
<link href="https://fonts.googleapis.com/css2?family=Montserrat:wght@300;400;500&display=swap" rel="stylesheet">
<style>
  :root {
    --backdrop: #ebeced;
    --card: #222222;
    --white: #ffffff;
    --soft-white: #e6e6e6;
    --muted: #b9b9b9;
    --accent-red: #c8102e;
  }
  * { margin: 0; padding: 0; box-sizing: border-box; }
  html, body {
    width: 1200px;
    height: 1200px;
    overflow: hidden;
    background: var(--backdrop);
    font-family: "Montserrat", sans-serif;
  }
  .card {
    position: absolute;
    left: 180px;
    width: 840px;
    height: 480px;
    border-radius: 24px;
    background: var(--card);
  }
  .card-front { top: 62px; }
  .card-back { top: 606px; }

  .brand-name {
    position: absolute;
    left: 0;
    right: 0;
    top: 222px;
    text-align: center;
    font-size: 30px;
    font-weight: 400;
    letter-spacing: 0.28em;
    color: var(--soft-white);
  }

  .person-name {
    position: absolute;
    right: 458px;
    top: 150px;
    text-align: right;
    line-height: 1.2;
  }
  .person-first {
    display: block;
    font-size: 36px;
    font-weight: 500;
    color: var(--white);
  }
  .person-last {
    display: block;
    font-size: 34px;
    font-weight: 300;
    color: var(--soft-white);
  }

  .divider {
    position: absolute;
    left: 419px;
    top: 138px;
    width: 3px;
    height: 202px;
    background: var(--accent-red);
  }

  .contact-list {
    position: absolute;
    left: 466px;
    top: 166px;
    list-style: none;
  }
  .contact-item {
    display: flex;
    align-items: center;
    height: 38.5px;
    font-size: 19px;
    font-weight: 400;
    color: var(--soft-white);
  }
  .contact-icon {
    width: 22px;
    height: 22px;
    margin-right: 8px;
    flex: none;
  }

  .services {
    position: absolute;
    left: 0;
    right: 0;
    top: 418px;
    text-align: center;
    font-size: 20px;
    font-weight: 300;
    color: var(--muted);
    letter-spacing: 0.01em;
  }
</style>
</head>
<body>

<section class="card card-front">
  <div class="brand-name">KESTREL REHAB</div>
</section>

<section class="card card-back">
  <div class="person-name">
    <span class="person-first">DAMON</span>
    <span class="person-last">WHITLOCK JR</span>
  </div>

  <div class="divider"></div>

  <ul class="contact-list">
    <li class="contact-item">
      <svg class="contact-icon" viewBox="0 0 22 22" aria-hidden="true">
        <rect x="2" y="5" width="18" height="12" fill="none" stroke="#fff" stroke-width="1.6"/>
        <polyline points="2,5 11,12 20,5" fill="none" stroke="#fff" stroke-width="1.6"/>
      </svg>
      dwhitlockjr@mailbox.com
    </li>
    <li class="contact-item">
      <svg class="contact-icon" viewBox="0 0 22 22" aria-hidden="true">
        <circle cx="11" cy="11" r="8" fill="none" stroke="#fff" stroke-width="1.8"/>
      </svg>
      @Kestrel_Rehab_
    </li>
    <li class="contact-item">
      <svg class="contact-icon" viewBox="0 0 22 22" aria-hidden="true">
        <g fill="none" stroke="#fff" stroke-width="1.5">
          <circle cx="11" cy="11" r="8.5"/>
          <ellipse cx="11" cy="11" rx="3.8" ry="8.5"/>
          <line x1="2.5" y1="11" x2="19.5" y2="11"/>
          <path d="M4.2 6.5h13.6M4.2 15.5h13.6"/>
        </g>
      </svg>
      www.kestrelrehab.com
    </li>
    <li class="contact-item">
      <svg class="contact-icon" viewBox="0 0 22 22" aria-hidden="true">
        <path d="M6.2 2.5l2.6 4.2-1.8 1.8c1 2.4 3 4.4 5.4 5.4l1.8-1.8 4.2 2.6-1.2 3.2c-.4.8-1.2 1.2-2 1.1C8.6 18.4 3.6 13.4 3 6.8c-.1-.8.3-1.6 1.1-2z" fill="#fff"/>
      </svg>
      555-014-2730
    </li>
  </ul>

  <p class="services">General Contractor • Home Remodel • Concrete Alternatives</p>
</section>

</body>
</html>
```